2 Page Business Flyer for Finance Business

Need a two page flyer created for a finance business. Lots of text and needs to fit on two pages.

Corporate business/banking look and feel. Not too many large images. Lots of white space, clean design. Attached is color palette and the text contents of the flyer.

```html
<!DOCTYPE html>
<html lang="en">
<head>
<meta charset="utf-8">
<title>Vanilla Option Flyer</title>
<link href="https://fonts.googleapis.com/css2?family=Roboto+Condensed:wght@300;400;500&family=Roboto:wght@300&display=swap" rel="stylesheet">
<style>
:root{
  --stage:#5b5b5b;
  --paper:#ffffff;
  --red:#c0262d;
  --gold:#d5c28f;
  --gold-soft:#efe7d3;
  --dark:#333333;
  --ink:#2b2b2b;
  --photo-a:#4a3a2e;
  --photo-b:#8c7a67;
}
*{box-sizing:border-box;margin:0;padding:0}
html,body{width:1200px;height:835px;overflow:hidden;background:var(--stage)}
body{position:relative;font-family:"Roboto Condensed",sans-serif;color:var(--ink)}
.page{position:absolute;top:42px;width:507px;height:718px;background:var(--paper);overflow:hidden;box-shadow:0 2px 8px rgba(0,0,0,.35)}
.page--front{left:56px}
.page--back{left:630px}
.page-label{position:absolute;top:776px;width:507px;text-align:center;font-family:"Roboto",sans-serif;font-weight:300;font-size:35px;color:#fff}
.page-label--front{left:56px}
.page-label--back{left:630px}
.abs{position:absolute}
.heading{border-left:4px solid var(--gold);padding-left:9px;font-size:19px;line-height:21px;font-weight:400;color:var(--ink)}
.heading .accent{color:var(--red)}
.body-text{font-size:8.7px;line-height:12.2px;font-weight:300;text-align:justify;color:var(--ink)}
.body-text p+p{margin-top:5px}
.drop{font-size:22px;line-height:16px;float:left;margin-right:1px;font-weight:300}
.checks{list-style:none}
.checks li{position:relative;padding-left:16px;font-size:8.7px;line-height:12px;font-weight:300}
.checks li+li{margin-top:5px}
.checks li::before{content:"";position:absolute;left:0;top:2px;width:7px;height:7px;border:1px solid var(--red)}
.checks li::after{content:"";position:absolute;left:3px;top:1px;width:3px;height:6px;border:solid var(--red);border-width:0 1.3px 1.3px 0;transform:rotate(40deg)}
.checks--light li{color:#fff}
.checks--light li::before,.checks--light li::after{border-color:var(--gold)}
.dark-band{background:var(--dark)}
.example-banner{background:var(--gold);border-bottom-right-radius:14px;color:#fff;font-size:19px;line-height:21px;padding:10px 0 0 21px}
.section-title{font-size:19px;font-weight:400;text-align:center}
.gold-flank::before,.gold-flank::after{content:"";display:inline-block;width:4px;height:16px;background:var(--gold);vertical-align:-2px;margin:0 12px}
.factors{list-style:none}
.factors li{position:relative;height:18px;margin-bottom:4px;padding-left:19px;font-size:8.7px;line-height:18px;font-weight:400}
.factors li span{display:block;height:100%;padding-left:6px;background:linear-gradient(90deg,#f3e1e3 0%,#f8eced 50%,rgba(255,255,255,0) 100%)}
.factors li::before{content:"";position:absolute;left:0;top:5px;width:7px;height:7px;border:1px solid var(--red)}
.factors li::after{content:"";position:absolute;left:3px;top:4px;width:3px;height:6px;border:solid var(--red);border-width:0 1.3px 1.3px 0;transform:rotate(40deg)}
</style>
</head>
<body>

<section class="page page--front">
  <svg class="abs" style="left:0;top:0" width="507" height="718" viewBox="0 0 507 718">
    <defs>
      <linearGradient id="deskTone" x1="0" y1="0" x2="1" y2="1">
        <stop offset="0" stop-color="#8c7a67"/>
        <stop offset="1" stop-color="#4a3a2e"/>
      </linearGradient>
    </defs>
    <polygon points="232,0 328,0 290,72" fill="#efe7d3"/>
    <polygon role="img" aria-label="Photo of a business handshake over a desk with laptop and contracts" points="328,0 507,0 507,326 216,326" fill="url(#deskTone)"/>
    <rect x="0" y="220" width="262" height="106" fill="#333333"/>
    <polygon points="262,220 262,326 216,326 258,220" fill="#333333"/>
    <path role="img" aria-label="Photo of a hand signing a document beside a laptop" d="M0,660 L60,660 Q68,602 100,602 L430,602 Q450,602 458,640 L466,660 L507,660 L507,718 L0,718 Z" fill="#2e2d2c"/>
  </svg>

  <h2 class="heading abs" style="left:21px;top:20px"><span class="accent">How does a Vanilla</span><br>Option contract work?</h2>

  <div class="body-text abs" style="left:22px;top:77px;width:232px">
    <p><span class="drop">T</span>he buyer of a vanilla option receives protection against an adverse movement in the exchange rate while allowing full participation in a beneficial move. At no time is the buyer of a Vanilla Option obligated to exercise the Option and transact the currencies, therefore providing flexibility in cases where the requirement to purchase foreign currency is not certain.</p>
    <p>A buyer of vanilla options is required to pay a premium (like an insurance premium) for the right, but not the obligation, to exchange currency at a predetermined rate on a predetermined date.</p>
  </div>

  <ul class="checks checks--light abs" style="left:23px;top:232px;width:192px">
    <li>Set a protection rate which will be your worst-case scenario at expiry</li>
    <li>Determine the amount of currency you wish to protect</li>
    <li>Choose an expiry date for the contract</li>
    <li>Calculate the premium you are required to pay</li>
  </ul>

  <div class="abs" style="left:0;top:326px;width:507px;height:6px;background:var(--gold)"></div>
  <div class="example-banner abs" style="left:0;top:326px;width:252px;height:64px">Let’s look at an example:<br>YOU ARE IN IMPORTER.</div>

  <div class="body-text abs" style="left:22px;top:410px;width:212px">
    <p><span class="drop">Y</span>our construction company has bid on a project that if successful, will require you to import materials from the United States to use in construction. You have used todays pricing of materials in calculating your bid and want to protect against an adverse move in the US dollar exchange rate from eroding your margin if your bid is chosen for the project.</p>
    <p>You choose to buy a Vanilla Call which will protect you from a rise in the USD/CAD exchange rate above your protection rate. You choose to buy protection on $500,000 USD, with a protection rate (strike rate) of 1.3300 expiring 3 months from now. You are required to pay a premium which in this case is calculated to be 1.8%, or 11,970 CAD.</p>
  </div>

  <div class="body-text abs" style="left:268px;top:354px;width:213px">
    <p>Your bid is successful: If the exchange rate is below your protection rate at expiration, you have no obligation relating to the vanilla call and you are free to buy USD at the cheaper spot rate. If the exchange rate is above your protection rate, your have the right to purchase your USD at the protection rate, and thereby claiming your insurance policy.</p>
    <p>Your bid is not successful: You have no obligation relating to the vanilla option however, if at expiry the exchange rate is above the protection rate, you may exercise your right to buy USD at the lower rate and simultaneous sell USD back at the prevailing spot rate, thereby recouping some or all of the premium paid to buy the option. Alternatively, if you find out your bid was not successful with time still left until expiration, you may sell your option back into the market in the case that it still has residual value, which will depend on various market factors.</p>
  </div>
</section>

<section class="page page--back">
  <h2 class="heading abs" style="left:21px;top:20px;width:220px"><span class="accent">Characteristics</span></h2>
  <ul class="checks abs" style="left:21px;top:52px;width:198px">
    <li>You are looking for a straight-forward hedging solution</li>
    <li>You want to receive full benefit from an appreciation of the currency you are exposed to</li>
    <li>You are comfortable receiving protection at the strike rate of the option</li>
    <li>You are willing to pay the non-refundable premium</li>
  </ul>

  <h2 class="heading abs" style="left:259px;top:20px;width:230px">Advantages</h2>
  <ul class="checks abs" style="left:259px;top:52px;width:222px">
    <li>You hedge your foreign currency exposure at a predefined hedge rate</li>
    <li>You can choose the hedge rate that suits your budget requirements</li>
    <li>Provides the ability to fully participate in a favourable exchange rate move</li>
    <li>You can choose from most major currency pairs to meet your needs</li>
  </ul>

  <h2 class="section-title gold-flank abs" style="left:0;top:178px;width:507px">Advantages</h2>
  <p class="body-text abs" style="left:0;top:208px;width:507px;text-align:center">Premium paid is non-refundable and remains your only obligation when buying vanilla options</p>

  <div class="dark-band abs" style="left:0;top:234px;width:507px;height:112px"></div>
  <h2 class="section-title abs" style="left:0;top:246px;width:507px;color:var(--gold)">Why use Vanilla Options?</h2>
  <p class="body-text abs" style="left:28px;top:276px;width:451px;text-align:center;color:#fff">Vanilla options are often compared to an insurance product. The buyer pays a non-refundable premium for the right, but not the obligation to trade currency in the future at the protection rate of the option. This product allows you to participate in a beneficial move to an unlimited extent, which will be the most advantageous outcome, if the exchange rate moves in your favour enough to more than offset the premium paid for the option.</p>

  <h2 class="heading abs" style="left:25px;top:363px"><span class="accent">What determines the</span><br>price of a Vanilla Option?</h2>
  <p class="body-text abs" style="left:22px;top:415px;width:461px">The cost of an option is defined by the premium that is required to be paid in order to enter into the contract. Premiums are calculated using the industry standard formulas based upon the Black Scholes model. The most important variables in the option pricing formulas include the following:</p>

  <ul class="factors abs" style="left:22px;top:461px;width:440px">
    <li><span>The current market Spot Rate.</span></li>
    <li><span>Market volatility – the higher the volatility, the higher the premium.</span></li>
    <li><span>The Term of the Option – a longer term typically results in a higher premium.</span></li>
    <li><span>The Strike Rate – the closer to being ITM the protection rate is, the higher the premium.</span></li>
    <li><span>The interest rate differential of the two currencies involved.</span></li>
    <li><span>Style – European or American, or whether the option can be exercised prior to expiration</span></li>
  </ul>

  <p class="body-text abs" style="left:21px;top:604px;width:462px">An option can either a European (meaning that they can only be exercised on the expiry date), or American (meaning that they can be exercised at any time prior to expiration). We normally deals in European options however, we do offer American options under certain circumstances and when specific delivery terms are agreed upon between us and the customer.</p>

  <svg class="abs" style="left:0;top:660px" width="507" height="58" viewBox="0 0 507 58">
    <path d="M0,30 L50,30 Q60,5 92,5 L430,5 Q460,5 470,30 L507,30 L507,58 L0,58 Z" fill="#d5c28f"/>
  </svg>
</section>

<div class="page-label page-label--front">Front</div>
<div class="page-label page-label--back">Back</div>

</body>
</html>
```